Maple Grin
Pediatric and Family Dentistry
Maple Grin -
Creative Brief
Bright & Fun-filled
Doria Velcott, DMD
Pediatric Dentist
1746 Brannock Lane, Suite 410 Linwood Falls, OR 22157
maplegrinoffice@brindlemail.com
MapleGrinClinic.com
We would like a second name on this card as listed below Name: Lorna Tevick, DDS Title: General Dentist
Appointment For: Date: Time:

```html
<!DOCTYPE html>
<html lang="en">
<head>
<meta charset="utf-8">
<title>Maple Grin – Stationery Set</title>
<link href="https://fonts.googleapis.com/css2?family=Open+Sans:wght@400;600;700&display=swap" rel="stylesheet">
<style>
:root{
  --bg:#e7e4df;
  --paper:#ffffff;
  --ink:#3a3a3a;
  --muted:#777777;
  --black:#141414;
  --orange:#f7941d;
  --yellow:#ffc20e;
  --shadow:0 4px 12px rgba(0,0,0,.18);
}
*{box-sizing:border-box;margin:0;padding:0}
html,body{width:1200px;height:731px;overflow:hidden}
body{background:var(--bg);font-family:"Open Sans",Arial,sans-serif;color:var(--ink);position:relative}

/* logo */
.logo{display:flex;align-items:center;gap:5px}
.logo-mark{width:14px;height:14px;border-radius:50%;background:var(--yellow);flex:none}
.logo-name{font-weight:700;color:var(--orange);font-size:17px;line-height:1;white-space:nowrap}
.logo-tag{font-size:5.5px;color:var(--muted);margin-top:2px;white-space:nowrap}

/* business cards */
.card{position:absolute;left:70px;width:240px;height:136px;background:var(--paper);box-shadow:var(--shadow);border-radius:4px;overflow:hidden}
.card.dark{background:var(--black);color:#e6e6e6}
.card.dark .logo-tag{color:#bbbbbb}
.card-front .logo{position:absolute;left:14px;top:48px}
.card-details{position:absolute;left:128px;top:14px;font-size:5.6px;line-height:1.55}
.card-details .name{font-weight:700;font-size:6.4px}
.card-details .gap{height:5px}
.band{position:absolute;left:0;right:0;bottom:0;height:9px;border-top:2px solid var(--yellow);background:transparent}
.band .site{position:absolute;right:0;bottom:0;height:7px;width:45%;background:var(--orange);color:#fff;font-size:5px;line-height:7px;text-align:right;padding-right:6px;clip-path:polygon(6% 0,100% 0,100% 100%,0 100%)}
.card-back .logo{position:absolute;right:14px;top:14px}
.card-back .logo-name{font-size:13px}
.card-back .logo-mark{width:11px;height:11px}
.appt{position:absolute;left:14px;top:46px;font-size:6.5px;line-height:1.9}
.appt h3{font-size:11px;font-weight:600;margin-bottom:2px}
.appt .line{display:inline-block;border-bottom:1px solid currentColor;width:110px;height:6px;vertical-align:baseline}
.appt .short{width:60px}
.appt .box{display:inline-block;width:14px;border-bottom:1px solid currentColor;height:6px;margin:0 2px}

/* letterhead */
.sheet{position:absolute;background:var(--paper);box-shadow:var(--shadow)}
.sheet-back{left:392px;top:66px;width:340px;height:440px}
.letterhead{left:372px;top:86px;width:340px;height:440px}
.letterhead .logo{position:absolute;left:22px;top:24px}
.letterhead .logo-name{font-size:18px}
.lh-address{position:absolute;right:22px;top:22px;font-size:5.2px;line-height:1.55;color:var(--muted)}
.letterhead .band{height:12px;bottom:6px}
.letterhead .band .site{height:9px;line-height:9px;font-size:5.6px}

/* envelopes */
.env{position:absolute;left:770px;width:370px;height:150px;background:var(--paper);box-shadow:var(--shadow);overflow:hidden}
.env svg{position:absolute;left:0;top:0}
.env .flap-mark{position:absolute;left:50%;top:12px;width:18px;height:18px;margin-left:-9px;border-radius:50%;border:2px solid #fff}
.env-orange{top:86px}
.env-black{top:166px}
.env-white{top:246px}
.env-white .flap-mark{border-color:var(--orange)}
.env-front{top:326px;height:160px}
.env-front .logo{position:absolute;left:18px;top:20px}
.env-front .logo-name{font-size:14px}
.env-front .ret{position:absolute;left:18px;top:48px;font-size:5px;line-height:1.5;color:var(--muted)}
.env-front .band{height:11px;bottom:6px}
.env-front .band .site{height:8px;line-height:8px;font-size:5.4px}
</style>
</head>
<body>

<!-- Business card front (light) -->
<section class="card card-front" style="top:60px">
  <div class="logo"><span class="logo-mark"></span><div><div class="logo-name">Maple Grin</div><div class="logo-tag">Pediatric and Family Dentistry</div></div></div>
  <div class="card-details">
    <div class="name">Doria Velcott, DMD</div><div>Pediatric Dentist</div>
    <div class="name">Lorna Tevick, DDS</div><div>General Dentist</div>
    <div class="gap"></div>
    <div>1746 Brannock Lane, Suite 410</div><div>Linwood Falls, OR 22157</div>
    <div>Phone: (555) 555-0186</div>
    <div>maplegrinoffice@brindlemail.com</div>
  </div>
  <div class="band"><div class="site">MapleGrinClinic.com</div></div>
</section>

<!-- Business card back (light) -->
<section class="card card-back" style="top:220px">
  <div class="logo"><span class="logo-mark"></span><div><div class="logo-name">Maple Grin</div><div class="logo-tag">Pediatric and Family Dentistry</div></div></div>
  <div class="appt">
    <h3>Appointment</h3>
    <div>For: <span class="line"></span></div>
    <div>Date: <span class="line"></span></div>
    <div>Time: <span class="line short"></span> <span class="box"></span>Am <span class="box"></span>Pm</div>
  </div>
  <div class="band"><div class="site">MapleGrinClinic.com</div></div>
</section>

<!-- Business card front (dark) -->
<section class="card card-front dark" style="top:380px">
  <div class="logo"><span class="logo-mark"></span><div><div class="logo-name">Maple Grin</div><div class="logo-tag">Pediatric and Family Dentistry</div></div></div>
  <div class="card-details">
    <div class="name">Doria Velcott, DMD</div><div>Pediatric Dentist</div>
    <div class="name">Lorna Tevick, DDS</div><div>General Dentist</div>
    <div class="gap"></div>
    <div>1746 Brannock Lane, Suite 410</div><div>Linwood Falls, OR 22157</div>
    <div>Phone: (555) 555-0186</div>
    <div>maplegrinoffice@brindlemail.com</div>
  </div>
  <div class="band"><div class="site">MapleGrinClinic.com</div></div>
</section>

<!-- Business card back (dark) -->
<section class="card card-back dark" style="top:540px">
  <div class="logo"><span class="logo-mark"></span><div><div class="logo-name">Maple Grin</div><div class="logo-tag">Pediatric and Family Dentistry</div></div></div>
  <div class="appt">
    <h3>Appointment</h3>
    <div>For: <span class="line"></span></div>
    <div>Date: <span class="line"></span></div>
    <div>Time: <span class="line short"></span> <span class="box"></span>Am <span class="box"></span>Pm</div>
  </div>
  <div class="band"><div class="site">MapleGrinClinic.com</div></div>
</section>

<!-- Letterhead -->
<div class="sheet sheet-back"></div>
<section class="sheet letterhead">
  <div class="logo"><span class="logo-mark"></span><div><div class="logo-name">Maple Grin</div><div class="logo-tag">Pediatric and Family Dentistry</div></div></div>
  <div class="lh-address">
    <div>1746 Brannock Lane, Suite 410</div><div>Linwood Falls, OR 22157</div>
    <div>Phone: (555) 555-0186</div>
    <div>maplegrinoffice@brindlemail.com</div>
  </div>
  <div class="band"><div class="site">MapleGrinClinic.com</div></div>
</section>

<!-- Envelope backs -->
<section class="env env-orange">
  <svg width="370" height="150" viewBox="0 0 370 150"><polygon points="0,0 370,0 185,80" fill="var(--orange)"/><polyline points="0,150 185,70 370,150" fill="none" stroke="#ddd"/></svg>
  <span class="flap-mark"></span>
</section>
<section class="env env-black">
  <svg width="370" height="150" viewBox="0 0 370 150"><polygon points="0,0 370,0 185,80" fill="var(--black)"/><polyline points="0,150 185,70 370,150" fill="none" stroke="#ddd"/></svg>
  <span class="flap-mark" style="border-color:var(--yellow)"></span>
</section>
<section class="env env-white">
  <svg width="370" height="150" viewBox="0 0 370 150"><polygon points="0,0 370,0 185,80" fill="#fafafa" stroke="#cfcfcf"/></svg>
  <span class="flap-mark"></span>
</section>

<!-- Envelope front -->
<section class="env env-front">
  <div class="logo"><span class="logo-mark"></span><div><div class="logo-name">Maple Grin</div><div class="logo-tag">Pediatric and Family Dentistry</div></div></div>
  <div class="ret"><div>1746 Brannock Lane, Suite 410</div><div>Linwood Falls, OR 22157</div></div>
  <div class="band"><div class="site">MapleGrinClinic.com</div></div>
</section>

</body>
</html>
```